Need a fun and informative infographic!

We need an infographic to describe our "client experience" which consists of 4 phases - see info about each of our "phases" which includes our available suite of services. UPDATED THE TEXT IN A NEW FILE CALLED "Client Experience Infographic Info".

We intend to use the infographic in both print and digital in a printed "leave behind", in packets for new clients, and possible on the website.

Lantern Tutors www.lanterntutors.example

Target Market(s)

Families of children aged Kindergarten through 12th Grade; affluent communities who have expendable income to spend on private tutoring and test prep.

Industry/Entity Type

Education

Font styles to use
Sans Serif

Requirements
Must have
• My project must use our brand colors.
• Light Blue CMYK: 60 27 0 0 RGB: 115 165 215
• Dark Blue CMYK: 93 85 36 27 RGB: 43 57 94
• Orange CMYK: 0 46 77 10 RGB: 230 125 53

```html
<!DOCTYPE html>
<html lang="en">
<head>
<meta charset="utf-8">
<title>Lantern Tutors – The Client Experience</title>
<link rel="stylesheet" href="https://fonts.googleapis.com/css2?family=Nunito:wght@700;800;900&family=Nunito+Sans:wght@300;400;600;700;800&display=swap">
<style>
  :root{
    --light-blue:#73a5d7;
    --blue:#5b97d2;
    --dark-blue:#2b395e;
    --orange:#e67d35;
    --text:#222831;
    --white:#ffffff;
    --placeholder:#dbe8f5;
  }
  *{box-sizing:border-box;margin:0;padding:0}
  html,body{width:800px;height:1200px;overflow:hidden;background:var(--white)}
  body{position:relative;font-family:"Nunito Sans",Arial,sans-serif;color:var(--text)}
  .abs{position:absolute}

  /* header */
  .brand{left:120px;top:50px;display:flex;align-items:center;gap:12px}
  .brand-dot{width:44px;height:44px;border-radius:50%;background:var(--dark-blue)}
  .brand-name{font-family:"Nunito Sans",sans-serif;font-weight:400;font-size:44px;color:var(--dark-blue);letter-spacing:-0.5px}
  .header-url{right:52px;top:106px;font-size:20px;color:var(--dark-blue);font-weight:400}

  .title-band{left:0;top:142px;width:800px;height:78px;background:var(--blue);display:flex;align-items:center;justify-content:center;color:var(--white);font-size:46px;letter-spacing:1px}
  .title-band b{font-weight:800;margin-right:14px}
  .title-band span{font-weight:300}

  /* cards */
  .card{border:2px dashed var(--light-blue);border-radius:22px}
  .card-title{font-family:"Nunito",sans-serif;font-weight:800;color:var(--dark-blue);font-size:26px;background:var(--white);padding:0 12px;line-height:1.15}
  .step{width:66px;height:66px;border-radius:50%;background:var(--orange);color:var(--white);font-family:"Nunito",sans-serif;font-weight:900;font-size:40px;display:flex;align-items:center;justify-content:center}
  .art{background:var(--placeholder);border-radius:14px}
  .copy{font-size:13.2px;line-height:1.32;color:var(--text)}
  .justify{text-align:justify}

  .checks{display:grid;grid-template-columns:112px 120px;row-gap:14px;font-size:15px}
  .check{display:flex;align-items:center;gap:8px}
  .tick{width:18px;height:18px;flex:none}

  .services{background:var(--blue);border-radius:24px}
  .services-title{font-family:"Nunito",sans-serif;font-weight:800;color:var(--white);font-size:27px;line-height:1.2}
  .services .copy{color:var(--white)}
  .service-list{display:flex;flex-direction:column;gap:12px;color:var(--white);font-weight:700;font-size:14.5px}
  .art-light{background:rgba(255,255,255,.28);border-radius:14px}

  /* footer */
  .footer{left:0;top:1140px;width:800px;height:48px;background:var(--blue);display:flex;align-items:center;justify-content:center;color:var(--white);font-size:16px}
  .footer .item{padding:0 14px;border-right:1px solid rgba(255,255,255,.8)}
  .footer .item:last-child{border-right:none;font-size:22px}
  .footer-strip{left:0;top:1188px;width:800px;height:12px;background:var(--orange)}
</style>
</head>
<body>

<svg width="0" height="0" class="abs" aria-hidden="true">
  <defs>
    <symbol id="tick" viewBox="0 0 20 20">
      <rect x="1.5" y="4.5" width="14" height="14" rx="1.5" fill="none" stroke="currentColor" stroke-width="2"/>
      <path d="M5 10.5l3.5 3.5L18.5 2.5" fill="none" stroke="currentColor" stroke-width="2.4" stroke-linecap="round" stroke-linejoin="round"/>
    </symbol>
  </defs>
</svg>

<header>
  <div class="abs brand"><div class="brand-dot"></div><div class="brand-name">lantern tutors</div></div>
  <div class="abs header-url">www.lanterntutors.example</div>
  <h1 class="abs title-band"><b>THE CLIENT</b><span>EXPERIENCE</span></h1>
</header>

<!-- Step 1 -->
<section class="abs card" style="left:35px;top:262px;width:357px;height:312px"></section>
<h2 class="abs card-title" style="left:80px;top:246px">The Consultation</h2>
<div class="abs art" style="left:55px;top:300px;width:140px;height:120px" role="img" aria-label="Line illustration of an educational director with a speech bubble"></div>
<div class="abs step" style="left:262px;top:304px">1</div>
<p class="abs copy" style="left:208px;top:410px;width:180px">The process begins with a complimentary and thorough consultation.</p>
<p class="abs copy" style="left:64px;top:479px;width:316px">One of our local Educational Directors meets in-person ( or via VideoLink if necessary ) with the parents and student to become acquainted and to better understand the family’s needs.</p>

<!-- Step 2 -->
<section class="abs card" style="left:413px;top:262px;width:356px;height:312px"></section>
<h2 class="abs card-title" style="left:492px;top:240px;text-align:center">Match and<br>Customize</h2>
<div class="abs art" style="left:445px;top:305px;width:170px;height:82px" role="img" aria-label="Line illustration of a group of students and tutors"></div>
<div class="abs step" style="left:672px;top:304px">2</div>
<p class="abs copy justify" style="left:440px;top:408px;width:312px">Students are matched with tutors based on understanding of each student's unique learning style, academic goals, and personality.</p>
<p class="abs copy justify" style="left:438px;top:469px;width:314px">The tutor(s) develop a personalized curriculum that aligns with the student's existing strengths and areas for improvement, while addressing all factors impacting performance such as test anxiety and self-confidence.</p>

<!-- Step 3 -->
<section class="abs card" style="left:35px;top:620px;width:357px;height:492px"></section>
<h2 class="abs card-title" style="left:115px;top:603px">Communication</h2>
<div class="abs art" style="left:64px;top:655px;width:220px;height:172px" role="img" aria-label="Line illustration of a student at a desk and a tutor, joined by arrows"></div>
<div class="abs step" style="left:300px;top:660px">3</div>
<p class="abs" style="left:88px;top:853px;font-size:18px">Tutoring sessions occur:</p>
<div class="abs checks" style="left:93px;top:890px;color:var(--text)">
  <div class="check"><svg class="tick" style="color:var(--orange)"><use href="#tick"/></svg>At home</div>
  <div class="check"><svg class="tick" style="color:var(--orange)"><use href="#tick"/></svg>Remotely</div>
  <div class="check"><svg class="tick" style="color:var(--orange)"><use href="#tick"/></svg>Our offices</div>
  <div class="check"><svg class="tick" style="color:var(--orange)"><use href="#tick"/></svg>Any location</div>
</div>
<div class="abs art" style="left:60px;top:960px;width:60px;height:68px" role="img" aria-label="Icon of hands holding a tablet"></div>
<p class="abs copy justify" style="left:134px;top:955px;width:244px">Our custom-built, mobile-friendly "Dashboard" provides parents with a thorough lesson summary after each session, convenient practice test registration, and real-time tracking of student progress.</p>

<!-- Services -->
<section class="abs services" style="left:413px;top:620px;width:356px;height:492px"></section>
<h2 class="abs services-title" style="left:463px;top:654px">Ongoing<br>Suite of<br>Services</h2>
<div class="abs art-light" style="left:630px;top:645px;width:100px;height:100px" role="img" aria-label="Icon of circular arrows above an open hand"></div>
<p class="abs copy justify" style="left:447px;top:770px;width:290px">Educational Directors are compassionate and responsive, ready to provide guidance and seamless coordination of whatever services the student requires.</p>
<p class="abs copy justify" style="left:447px;top:847px;width:240px">No matter where along the path our relationship begins, we can support students and families in a myriad of ways:</p>
<div class="abs service-list" style="left:483px;top:928px">
  <div class="check"><svg class="tick" style="color:var(--white)"><use href="#tick"/></svg>Standardized Test Prep</div>
  <div class="check"><svg class="tick" style="color:var(--white)"><use href="#tick"/></svg>Subject Tutoring</div>
  <div class="check"><svg class="tick" style="color:var(--white)"><use href="#tick"/></svg>College Admissions Consulting</div>
</div>
<p class="abs copy" style="left:447px;top:1027px;width:290px">When appropriate, we introduce behaviors for students to improve their executive functioning, organizational and time management.</p>

<!-- Footer -->
<footer>
  <div class="abs footer">
    <span class="item">LanternTutors</span>
    <span class="item">@LanternTutors</span>
    <span class="item">lantern.tutors</span>
    <span class="item">www.lanterntutors.example</span>
  </div>
  <div class="abs footer-strip"></div>
</footer>

</body>
</html>
```